Design layout of business card

Create a business card using existing logo and company information.
Our newly established business provides advice to family owned businesses for their succession planning, value improvement and also on business sales and acquisitions.

Target Market(s)

Owners of family businesses

Contact Information for Business Card

Key contact details are:
Greg Holloway
Director
P: 08 9342 5817
W: 0431 587 209
Address: Unit 4, 15 Kestrel Lane, Dunsborough, WA, 6281
Website: kinventureadvisory.com.au
Email: greg@kinventureadvisory.com.au

In smaller font somewhere needs to be these details:
ABN: 47 219 583 906
Licensed Real Estate & Business Agent No. RA53174
QTN Licensee Services Pty Ltd
AFSL No. 527361

Font styles to use
Sans Serif

Requirements
Must have
• Kin Venture Advisory logo to feature on front.
• Remaining logos to be included smaller and on back.
• Orla Business Sales logo to have words 'Powered by' next to it and to be the first of the uploaded logo files.
• Colours on card should complement the logo
Nice to have
• Clear and clean layout
• Logos for contact details for conciseness e.g. phone icon for mobile

```html
<!DOCTYPE html>
<html lang="en">
<head>
<meta charset="utf-8">
<title>Kin Venture Advisory – Business Card</title>
<link href="https://fonts.googleapis.com/css2?family=Montserrat:wght@600;700&family=Open+Sans:wght@400;600;700&display=swap" rel="stylesheet">
<style>
  :root {
    --orange: #e4532a;
    --grey: #8c9196;
    --ink: #2b2b2b;
    --paper: #f7f7f7;
    --backdrop: #e3e4e6;
    --white: #ffffff;
    --navy: #2f4a8a;
  }
  * { margin: 0; padding: 0; box-sizing: border-box; }
  html, body { width: 1200px; height: 1021px; overflow: hidden; }
  body {
    background: var(--backdrop);
    font-family: "Open Sans", sans-serif;
    color: var(--ink);
    position: relative;
  }
  .card {
    position: absolute;
    left: 290px;
    width: 620px;
    height: 354px;
    overflow: hidden;
    box-shadow: 0 4px 14px rgba(0,0,0,0.12);
  }

  /* Front */
  .card--front { top: 126px; background: var(--orange); color: var(--white); }
  .brand {
    position: absolute;
    display: flex;
    align-items: center;
    gap: 18px;
    font-family: "Montserrat", sans-serif;
    font-weight: 600;
    line-height: 0.98;
  }
  .brand__circle {
    border-radius: 50%;
    border-style: solid;
    flex: none;
  }
  .card--front .brand { left: 170px; top: 92px; font-size: 38px; color: var(--white); }
  .card--front .brand__circle { width: 112px; height: 112px; border-width: 5px; border-color: var(--white); }

  .partners {
    position: absolute;
    left: 60px; right: 60px; bottom: 42px;
    display: flex;
    align-items: center;
    justify-content: space-between;
  }
  .partner {
    font-family: "Open Sans", sans-serif;
    font-weight: 600;
    font-size: 15px;
    color: var(--white);
  }
  .badge {
    width: 58px; height: 58px;
    border-radius: 50%;
    background: var(--white);
    opacity: 0.9;
  }

  /* Back */
  .card--back { top: 540px; background: var(--paper); }
  .card--back .brand { left: 36px; top: 32px; font-size: 30px; color: var(--orange); gap: 14px; }
  .card--back .brand__circle { width: 90px; height: 90px; border-width: 4px; border-color: var(--grey); }

  .powered {
    position: absolute;
    left: 40px; top: 160px;
    display: flex;
    align-items: center;
    gap: 8px;
    font-size: 13px;
    font-style: italic;
  }
  .powered__badge {
    width: 34px; height: 34px;
    border-radius: 50%;
    border: 2px solid var(--navy);
    background: var(--white);
  }
  .legal {
    position: absolute;
    left: 40px; top: 204px;
    font-size: 12.5px;
    line-height: 1.3;
  }

  .person {
    position: absolute;
    right: 40px; top: 140px;
    text-align: right;
  }
  .person__name { font-size: 19px; font-weight: 700; color: var(--orange); line-height: 1.3; }
  .person__role { font-size: 14px; }

  .contact {
    position: absolute;
    right: 40px; bottom: 26px;
    text-align: right;
    font-size: 14px;
    line-height: 1.35;
  }
  .contact__address { margin-bottom: 8px; }
  .contact__line { display: flex; justify-content: flex-end; align-items: center; gap: 8px; }
  .contact__line svg { width: 15px; height: 15px; flex: none; }
  .icon { fill: none; stroke: var(--orange); stroke-width: 1.8; stroke-linecap: round; stroke-linejoin: round; }
  .icon--solid { fill: var(--orange); stroke: none; }
</style>
</head>
<body>

<section class="card card--front" aria-label="Card front">
  <div class="brand">
    <span class="brand__circle"></span>
    <span>Kin<br>Venture<br>Advisory</span>
  </div>
  <div class="partners">
    <span class="partner">Orla Group</span>
    <span class="partner">ABBN Brokers</span>
    <span class="badge"></span>
  </div>
</section>

<section class="card card--back" aria-label="Card back">
  <div class="brand">
    <span class="brand__circle"></span>
    <span>Kin<br>Venture<br>Advisory</span>
  </div>

  <div class="powered">Powered by <span class="powered__badge"></span></div>

  <p class="legal">
    ABN: 47 219 583 906<br>
    Licensed Real Estate &amp;<br>
    Business Agent No. RA53174<br>
    QTN Licensee Services Pty Ltd<br>
    AFSL No. 527361
  </p>

  <div class="person">
    <p class="person__name">Greg Holloway</p>
    <p class="person__role">Director</p>
  </div>

  <div class="contact">
    <p class="contact__address">Unit 4, 15 Kestrel Lane<br>Dunsborough, WA, 6281</p>
    <p class="contact__line">08 9342 5817
      <svg viewBox="0 0 16 16"><rect class="icon" x="4" y="1.5" width="8" height="13" rx="1.5"/><line class="icon" x1="7" y1="12" x2="9" y2="12"/></svg>
    </p>
    <p class="contact__line">0431 587 209
      <svg viewBox="0 0 16 16"><path class="icon--solid" d="M4 1.5l2.3 3-1.4 1.6c.8 1.9 2.2 3.4 4.1 4.3l1.6-1.4 3 2.3-1.4 2.4C7 13.5 2.5 9 1.6 3z"/></svg>
    </p>
    <p class="contact__line">greg@kinventureadvisory.com.au
      <svg viewBox="0 0 16 16"><rect class="icon" x="1.5" y="3.5" width="13" height="9"/><polyline class="icon" points="1.5,3.5 8,9 14.5,3.5"/></svg>
    </p>
    <p class="contact__line">kinventureadvisory.com.au
      <svg viewBox="0 0 16 16"><circle class="icon" cx="8" cy="8" r="6.5"/><ellipse class="icon" cx="8" cy="8" rx="2.8" ry="6.5"/><line class="icon" x1="1.5" y1="8" x2="14.5" y2="8"/></svg>
    </p>
  </div>
</section>

</body>
</html>
```